Blue Heron IT Business Card - Clean, Simple

Need a simple, clean standard sized business card for an IT consulting business using existing logo and company colours. Background should be mainly white. Feel free to be creative but clean, simple, quiet design is preferred. Font is specified in logo but any sans serif fonts work.

Contact Information for card is as follows (doesn't need to be in this exact order):

Martin Calloway
Owner
martin@blueheronit.ca
705-391-2586
www.blueheronit.ca

Target Market(s)

Small to medium sized business.

Industry/Entity Type

IT Consulting

Contact Information for Business Card

Logo and contact info.

Font styles to use
Sans Serif

Colors
EE7325
F08F49
F5BC92
FAE3D3
FDF4ED

Requirements
Must have
• All white or mostly white background.

```html
<!DOCTYPE html>
<html lang="en">
<head>
<meta charset="utf-8">
<title>Blue Heron IT – Business Card</title>
<link href="https://fonts.googleapis.com/css2?family=Raleway:wght@300;400;600&display=swap" rel="stylesheet">
<style>
  :root {
    --orange: #ee7325;
    --orange-light: #f08f49;
    --peach: #f5bc92;
    --charcoal: #3b3b3d;
    --charcoal-light: #555558;
    --ink: #333335;
    --paper: #ffffff;
    --muted: #e6e6e6;
    --backdrop: #8199b8;
  }
  * { margin: 0; padding: 0; box-sizing: border-box; }
  html, body { width: 1200px; height: 876px; overflow: hidden; }
  body {
    background: var(--backdrop);
    font-family: "Raleway", Arial, sans-serif;
    position: relative;
  }
  .card {
    position: absolute;
    width: 504px;
    height: 288px;
    box-shadow: 0 10px 24px rgba(30, 45, 70, 0.28);
    overflow: hidden;
  }

  /* Brand side */
  .card--brand {
    left: 620px;
    top: 130px;
    background: linear-gradient(135deg, var(--orange) 0%, var(--orange-light) 55%, var(--orange) 100%);
    color: var(--paper);
  }
  .card--brand .wordmark {
    position: absolute;
    left: 0; right: 0; top: 96px;
    text-align: center;
    font-size: 46px;
    font-weight: 600;
    letter-spacing: 0.5px;
  }
  .card--brand .website {
    position: absolute;
    left: 0; right: 0; top: 180px;
    text-align: center;
    font-size: 14px;
    font-weight: 400;
    letter-spacing: 6px;
  }
  .wordmark .dot {
    display: inline-block;
    width: 14px; height: 14px;
    border-radius: 50%;
    margin-right: 12px;
    vertical-align: middle;
    position: relative;
    top: -4px;
  }
  .card--brand .dot { background: var(--paper); }

  /* Contact side */
  .card--contact {
    left: 76px;
    top: 448px;
    background: var(--paper);
    display: flex;
  }
  .contact-panel {
    width: 210px;
    height: 100%;
    background: linear-gradient(150deg, var(--charcoal) 0%, var(--charcoal-light) 50%, var(--charcoal) 100%);
    color: var(--muted);
    padding: 30px 22px;
    text-align: right;
    position: relative;
  }
  .contact-panel .name {
    font-size: 15px;
    font-weight: 300;
    letter-spacing: 0.5px;
    text-transform: uppercase;
    white-space: nowrap;
  }
  .contact-panel .name .first { color: var(--orange); font-weight: 400; }
  .contact-panel .role {
    font-size: 11px;
    font-weight: 300;
    letter-spacing: 1px;
    text-transform: uppercase;
    margin-top: 4px;
  }
  .contact-panel .details {
    position: absolute;
    right: 22px;
    bottom: 32px;
    list-style: none;
    font-size: 12.5px;
    font-weight: 400;
    line-height: 1.7;
  }
  .logo-area {
    flex: 1;
    display: flex;
    align-items: center;
    justify-content: center;
  }
  .card--contact .wordmark {
    font-size: 32px;
    font-weight: 600;
    color: var(--ink);
    white-space: nowrap;
  }
  .card--contact .dot { background: var(--orange); width: 11px; height: 11px; margin-right: 10px; top: -3px; }
</style>
</head>
<body>
  <section class="card card--brand" aria-label="Business card, brand side">
    <div class="wordmark"><span class="dot"></span>Blue Heron IT</div>
    <div class="website">www.blueheronit.ca</div>
  </section>

  <section class="card card--contact" aria-label="Business card, contact side">
    <div class="contact-panel">
      <p class="name"><span class="first">Martin</span>Calloway</p>
      <p class="role">Owner</p>
      <ul class="details">
        <li>martin@blueheronit.ca</li>
        <li>705-391-2586</li>
      </ul>
    </div>
    <div class="logo-area">
      <div class="wordmark"><span class="dot"></span>Blue Heron IT</div>
    </div>
  </section>
</body>
</html>
```